Mirvald Health & Wellness needs a fresh and interesting website

I need a rebrand and redevelopment of my website, www.tessapinlowe.com
Our mission is provide bespoke , lifestyle medicine , everyone has their own path to health. and we are creating a personalized experience for people to life their life to the fullest
Mirvald - means sea lands
I need an landing page and about page and potentially a few project launch pages , I have been using Wordpress for my basic information and then I use Kartra for the launch pages of my programs since I can edit those easily.

Target Market(s)

Corporate and individual's who are interested in a different perspective on health and wellness , and living with a chronic illness

Industry/Entity Type

Health, lifestyle , wellness coaching and medicine

Coding

Number of Pages Required

2 page

Font styles to use
Other font styles liked:
• look into the logo

Requirements
Must have
• the logo I uploaded
Nice to have
• I want a fresh perspective on health, I have bamboo, hibiscus vibes in my logo , but also like more of a water vibe/ I want something earthy but not too boho it needs to be clean
Should not have
• every other holistic health vibe,

```html
<!DOCTYPE html>
<html lang="en">
<head>
<meta charset="utf-8">
<title>Mirvald Health &amp; Wellness</title>
<link href="https://fonts.googleapis.com/css2?family=Prata&family=Roboto:ital,wght@0,400;0,500;1,400&display=swap" rel="stylesheet">
<style>
:root{
  --stage:#b5cdd3;
  --white:#ffffff;
  --mist:#eaf3fc;
  --teal:#1aa6d0;
  --ink-blue:#196e8e;
  --navy:#07638e;
  --leaf:#66b515;
  --text:#6d6d6d;
  --dark:#2a2a2a;
  --serif:'Prata', Georgia, serif;
  --sans:'Roboto', Arial, sans-serif;
}
*{margin:0;padding:0;box-sizing:border-box}
html,body{width:1200px;height:3503px;overflow:hidden;background:var(--stage)}
.page{position:absolute;left:68px;top:0;width:1064px;height:3503px;background:var(--mist);font-family:var(--sans);color:var(--text)}
.abs{position:absolute}
.site-header{left:0;top:0;width:1064px;height:75px;background:var(--white)}
.brand{left:41px;top:17px;display:flex;align-items:center;gap:14px}
.brand-dot{width:40px;height:40px;border-radius:50%;background:var(--teal)}
.brand-name{font-family:var(--serif);font-size:30px;color:var(--ink-blue);letter-spacing:1px;line-height:1}
.nav-home{left:609px;top:20px;width:73px;height:40px;background:var(--teal);color:#fff;border-radius:3px;font-family:var(--serif);font-size:13px;display:flex;align-items:center;justify-content:center}
.nav-link{top:20px;height:40px;display:flex;align-items:center;font-family:var(--serif);font-size:13px;color:#333}
.nav-cta{left:889px;top:20px;width:146px;height:40px;border:2px solid var(--teal);border-radius:3px;color:var(--teal);font-size:14px;display:flex;align-items:center;justify-content:center}
.hero{left:0;top:75px;width:1064px;height:441px;background:linear-gradient(90deg,#3f7d3a 0%,#5f9b4c 35%,#8fae7a 55%,#b24a55 75%,#c9a99a 100%)}
.hero-panel{left:38px;top:167px;width:522px;height:288px;background:rgba(28,95,40,.78);border-radius:8px}
.hero-title{left:66px;top:200px;font-family:var(--serif);font-size:33px;color:#fff}
.hero-text{left:65px;top:265px;width:470px;font-size:14.5px;line-height:18px;color:#fff}
.hero-input{left:65px;top:343px;width:281px;height:38px;background:#fff;border-radius:3px 0 0 3px;font-size:14px;color:#aaa;padding-left:22px;display:flex;align-items:center}
.hero-btn{left:346px;top:343px;width:144px;height:38px;background:var(--teal);color:#fff;font-size:14px;display:flex;align-items:center;justify-content:center;border-radius:0 3px 3px 0}
.hero-note{left:66px;top:397px;font-size:10.5px;color:#fff}
.photo{background:linear-gradient(135deg,#d8d2c8,#a8a098)}
.row-title{font-family:var(--serif);font-size:18px;color:var(--ink-blue);line-height:22px}
.row-text{font-size:11px;line-height:16px;color:var(--text);text-align:justify}
.btn{background:var(--teal);color:#fff;font-size:12px;border-radius:4px;display:flex;align-items:center;justify-content:center}
.quote-band{left:0;top:1680px;width:1064px;height:153px;background:#fff}
.quote-text{left:120px;top:1730px;width:800px;font-size:11.5px;font-style:italic;color:#222;line-height:16px}
.qmark{font-family:var(--serif);font-size:28px;color:#222;line-height:1}
.blogs-title{left:0;top:1865px;width:1064px;text-align:center;font-family:var(--serif);font-size:40px;color:var(--ink-blue)}
.card{top:1972px;width:286px;height:420px;background:#fff}
.card-img{left:0;top:0;width:286px;height:190px}
.card-date{left:0;top:213px;width:53px;height:63px;background:#17b2b9;color:#fff;text-align:center;padding-top:10px;font-size:22px;line-height:22px}
.card-date small{display:block;font-size:10px;line-height:12px}
.card-meta{left:83px;top:222px;font-size:9px;color:#888}
.card-title{left:83px;top:254px;width:180px;font-family:var(--serif);font-size:11px;color:#222;line-height:14px}
.card-text{left:83px;top:284px;width:180px;font-size:9.5px;line-height:14px;color:var(--ink-blue)}
.card-more{left:83px;top:374px;font-size:9px;color:var(--teal)}
.video{left:45px;top:2467px;width:629px;height:347px;background:linear-gradient(180deg,#1f2937,#3a4654 60%,#1a2230)}
.video-caption{left:0;top:276px;width:629px;text-align:center;color:#fff;font-size:22px}
.mission{left:50px;top:2854px;width:963px;height:260px;background:#fff;box-shadow:0 3px 6px rgba(0,0,0,.12)}
.avatar{left:443px;top:26px;width:76px;height:76px;border-radius:50%;background:linear-gradient(135deg,#9a9a9a,#3d3d3d)}
.mission-text{left:0;top:128px;width:963px;text-align:center;font-size:11px;font-style:italic;color:#222;line-height:15px}
.signature{left:445px;top:210px;width:72px;height:30px;background:#e4e6ea;border-radius:4px}
.footer-left{left:0;top:3144px;width:260px;height:359px;background:var(--navy);color:#fff;text-align:right}
.footer-mid{left:260px;top:3144px;width:541px;height:359px;background:var(--leaf);color:#fff;text-align:center}
.footer-right{left:801px;top:3144px;width:263px;height:359px;background:var(--navy);color:#fff}
.f-head{font-family:var(--serif);font-size:16px;letter-spacing:.5px}
.f-rule{height:1px;background:rgba(255,255,255,.45)}
</style>
</head>
<body>
<main class="page">

  <header class="site-header abs">
    <div class="brand abs"><span class="brand-dot"></span><span class="brand-name">MIRVALD</span></div>
    <a class="nav-home abs">Home</a>
    <a class="nav-link abs" style="left:700px">About Us</a>
    <a class="nav-link abs" style="left:791px">Blog</a>
    <a class="nav-cta abs">REGISTER NOW</a>
  </header>

  <section class="hero abs" role="img" aria-label="Photo of a smiling woman in a red hat and pink shawl outdoors among greenery"></section>
  <div class="hero-panel abs"></div>
  <h1 class="hero-title abs">Fall Into YourSelf</h1>
  <p class="hero-text abs">Join us for a delightful retreat experience right in the heart of the city, as we come together to honor this season of harvest and letting go, a time to turn inward to expand.</p>
  <div class="hero-input abs">Email Address</div>
  <div class="hero-btn abs">REGISTER NOW</div>
  <p class="hero-note abs">Register to begin your Self-Discovery journey"</p>

  <!-- row 1 -->
  <h2 class="row-title abs" style="left:78px;top:598px">Dr Tessa M Pinlowe DACM, L.Ac</h2>
  <p class="row-text abs" style="left:78px;top:638px;width:395px">At a young age, I discovered the transformative power of Eastern Medicine when it helped me overcome lung concerns, propelling me toward my dreams as a young athlete. Years later, I faced a pivotal choice: How could I best serve and heal my community? The answer was crystal clear—Eastern Medicine.</p>
  <div class="btn abs" style="left:78px;top:798px;width:104px;height:35px">Read more..</div>
  <div class="photo abs" style="left:531px;top:576px;width:482px;height:272px;background:linear-gradient(135deg,#cfcfcf,#4a4a4a)" role="img" aria-label="Black and white portrait of the doctor wearing a hat"></div>

  <!-- row 2 -->
  <div class="photo abs" style="left:51px;top:856px;width:480px;height:260px;background:linear-gradient(135deg,#f4f2ef,#d9c3ad)" role="img" aria-label="Acupuncture model of a shoulder with needles"></div>
  <h2 class="row-title abs" style="left:579px;top:888px">Traditional East Asian Medicine (TEAM)</h2>
  <p class="row-text abs" style="left:579px;top:928px;width:395px;text-align:left">As an Eastern Medicine doctor, I've had the privilege of positively impacting my community through integrative health choices.<br>My journey began after seven years of nurturing creativity and leadership in theatre costume design, when I made the life-altering decision to merge my love for art and science in the field of Acupuncture and Traditional East Asian Medicine (TEAM).</p>
  <div class="btn abs" style="left:579px;top:1064px;width:104px;height:34px">Read more..</div>

  <!-- row 3 -->
  <h2 class="row-title abs" style="left:80px;top:1133px">Masters of Oriental Medicine from<br>Northfield Health Sciences</h2>
  <p class="row-text abs" style="left:78px;top:1184px;width:422px">TEAM had profoundly healed me, and now I have the honor of using it to help others. With a Masters of Oriental Medicine from Northfield Health Sciences University and a Doctorate from Coastal College of Oriental Medicine, both with honors, I bring the highest level of expertise to my patients.<br>I hold national certification in the USA and am a licensed Acupuncturist and Doctor of Eastern Medicine. Beyond my academic achievements, I'm also an NLP coach, dedicated to bringing my best self to my patients and colleagues every day.</p>
  <div class="btn abs" style="left:78px;top:1333px;width:104px;height:34px">Read more..</div>
  <div class="photo abs" style="left:531px;top:1121px;width:482px;height:263px;background:linear-gradient(135deg,#8a7a66,#e6dcc4 50%,#c9c27a)" role="img" aria-label="Cup of herbal tea beside dried ginseng roots"></div>

  <!-- row 4 -->
  <div class="photo abs" style="left:51px;top:1386px;width:480px;height:263px;background:linear-gradient(135deg,#e8e8e6,#b9aea4)" role="img" aria-label="Woman lying down receiving an energy healing session"></div>
  <h2 class="row-title abs" style="left:561px;top:1409px">Join me on this journey of holistic healing</h2>
  <p class="row-text abs" style="left:561px;top:1446px;width:427px">While my "life list" is extensive, I find immense joy in travel, connecting with friends, mastering the bongos, practicing yoga &amp; Qi Gong, delving into Swedish language studies, and savoring the rhythms of salsa dancing. And, of course, I'm a devoted dog mom and take great pleasure in the ongoing adventure of remodeling our 1920s home.<br>Join me on this journey of holistic healing, where art, science, and compassion converge to create a healthier, happier community. Let's explore the profound possibilities of Eastern Medicine together!</p>
  <div class="btn abs" style="left:561px;top:1598px;width:103px;height:33px">Register Now</div>

  <!-- quote -->
  <section class="quote-band abs"></section>
  <span class="qmark abs" style="left:108px;top:1722px">“</span>
  <p class="quote-text abs">In meditation you try and let go of the past. You try to stop being anxious about the future . You focus on and enjoy the time you have now.<br>When you are stressed and burdened by things, it is liberating to tune into the present, to enter into the deeper rhythm of your being.</p>
  <span class="qmark abs" style="left:892px;top:1752px">”</span>
  <p class="abs" style="left:800px;top:1794px;font-size:9px;font-style:italic;color:#222">•&nbsp;&nbsp;Aldren Moyle</p>

  <!-- blogs -->
  <h2 class="blogs-title abs">Recent Blogs</h2>

  <article class="card abs" style="left:61px">
    <div class="card-img abs photo" style="background:linear-gradient(135deg,#8a7a66,#e6dcc4 50%,#c9c27a)" role="img" aria-label="Herbal tea with ginseng roots"></div>
    <div class="card-date abs">28<small>APR</small></div>
    <p class="card-meta abs">BY NIA / 6 COMMENTS</p>
    <h3 class="card-title abs">Practising yoga on the sea shore is a good method</h3>
    <p class="card-text abs">Mauris in erat justo. Nullam ac urna eu felis dapibus condimentum sit amet a augue. Sed non neque elit....</p>
    <p class="card-more abs">CONTINUE READING...</p>
  </article>
  <article class="card abs" style="left:389px">
    <div class="card-img abs photo" style="background:linear-gradient(135deg,#e8e8e6,#b9aea4)" role="img" aria-label="Woman receiving an energy healing session"></div>
    <div class="card-date abs">01<small>June</small></div>
    <p class="card-meta abs">BY NIA / 0 COMMENTS</p>
    <h3 class="card-title abs">Donec quis ex vel tincidunt</h3>
    <p class="card-text abs" style="top:272px">Mauris in erat justo. Nullam ac urna eu felis dapibus condimentum sit amet a augue. Sed non neque elit....</p>
    <p class="card-more abs">CONTINUE READING...</p>
  </article>
  <article class="card abs" style="left:718px">
    <div class="card-img abs photo" style="background:linear-gradient(135deg,#f4f2ef,#d9c3ad)" role="img" aria-label="Acupuncture shoulder model"></div>
    <div class="card-date abs">21<small>July</small></div>
    <p class="card-meta abs">BY NIA /3 COMMENTS</p>
    <h3 class="card-title abs">Integer diam gravida fringilla</h3>
    <p class="card-text abs" style="top:272px">Mauris in erat justo. Nullam ac urna eu felis dapibus condimentum sit amet a augue. Sed non neque elit....</p>
    <p class="card-more abs">CONTINUE READING...</p>
  </article>

  <!-- video -->
  <section class="video abs" role="img" aria-label="Video still of a person in a yoga pose before mountains at dusk">
    <svg class="abs" style="left:262px;top:124px" width="104" height="104" viewBox="0 0 104 104">
      <circle cx="52" cy="52" r="46" fill="none" stroke="rgba(255,255,255,.55)" stroke-width="6"/>
      <path d="M42 32 L74 52 L42 72 Z" fill="rgba(255,255,255,.55)"/>
    </svg>
    <p class="video-caption abs">Make Your Way To Complete Health</p>
  </section>
  <h2 class="row-title abs" style="left:695px;top:2467px;font-size:17px;line-height:21px">Make your way to complete<br>health</h2>
  <p class="row-text abs" style="left:695px;top:2527px;width:292px;font-size:10px;line-height:18.5px">Lorem ipsum dolor sit amet, consectetuer adipiscing elit, sed diam nonummy nibh euismod tincidunt ut laoreet dolore. Phasellus viverra nulla ut metus varius laoreet. Aenean the secrece is to fill most of the part with amazing fillers imperdiet. We at SOLVA provide various services to the nature of the clients.</p>
  <div class="btn abs" style="left:695px;top:2662px;width:103px;height:33px">Register Now</div>

  <!-- mission -->
  <section class="mission abs">
    <div class="avatar abs" role="img" aria-label="Round portrait of the doctor"></div>
    <span class="qmark abs" style="left:275px;top:121px;font-size:24px">“</span>
    <p class="mission-text abs">My mission is to cultivate a nurturing space that empowers people to find the<br>courage to soar in life while fostering strong, supportive communities.<br><br>Thank you for being a part of this journey!</p>
    <span class="qmark abs" style="left:668px;top:136px;font-size:24px">”</span>
    <div class="signature abs" role="img" aria-label="Handwritten signature of Tessa"></div>
  </section>

  <!-- footer -->
  <footer>
    <div class="footer-left abs">
      <p class="f-head abs" style="right:22px;top:3233px;top:52px">WORK HOURS</p>
      <div class="f-rule abs" style="left:125px;top:78px;width:113px"></div>
      <p class="abs" style="right:22px;top:84px;font-size:9.5px">Friday &amp; Saturday</p>
      <p class="abs" style="right:22px;top:99px;font-size:17px">0600 - 0900 hrs</p>
      <div class="f-rule abs" style="left:125px;top:126px;width:113px"></div>
      <p class="abs" style="right:22px;top:139px;font-size:9.5px">And all the Sundays</p>
      <p class="abs" style="right:22px;top:155px;font-size:17px">Will be Holidays</p>
      <p class="abs" style="right:22px;top:200px;width:215px;font-size:9.5px;line-height:13px;text-align:center">Non-Discrimination Policy | Privacy Policy | Terms of Use</p>
    </div>

    <div class="footer-mid abs">
      <div class="abs" style="left:253px;top:24px;width:36px;height:36px;border-radius:50%;border:2px solid #fff"></div>
      <p class="abs" style="left:0;top:70px;width:541px;font-family:var(--serif);font-size:26px;letter-spacing:1px">MIRVALD</p>
      <p class="abs" style="left:0;top:103px;width:541px;font-size:7px;letter-spacing:3px">HEALTH &amp; WELLNESS</p>
      <p class="abs" style="left:30px;top:122px;width:481px;font-size:10.5px;line-height:13.5px">We are thrilled to announce our partnership with Linden Row House for this extraordinary experience! They offer a serene and relaxing space right in the heart of Riverton. If you'd like to turn this day into a delightful weekend getaway, don't hesitate to reach out to them for overnight accommodation. Linden Row House is conveniently located near numerous amazing places for adventures, dining, and art.</p>
      <p class="abs" style="left:0;top:260px;width:541px;font-size:10px">© 2023 MIRVALD Health and wellness</p>
    </div>

    <div class="footer-right abs">
      <p class="f-head abs" style="left:57px;top:36px">CONTACT US</p>
      <svg class="abs" style="left:20px;top:76px" width="16" height="16" viewBox="0 0 24 24"><path d="M6.6 10.8a15 15 0 006.6 6.6l2.2-2.2a1 1 0 011-.25 11.4 11.4 0 003.6.6 1 1 0 011 1V20a1 1 0 01-1 1A17 17 0 013 4a1 1 0 011-1h3.5a1 1 0 011 1 11.4 11.4 0 00.6 3.6 1 1 0 01-.25 1z" fill="none" stroke="#fff" stroke-width="1.6"/></svg>
      <p class="abs" style="left:57px;top:77px;font-size:11.5px">Toll Free: 1450 3381</p>
      <svg class="abs" style="left:20px;top:115px" width="16" height="14" viewBox="0 0 24 20"><rect x="2" y="2" width="20" height="16" rx="1" fill="none" stroke="#fff" stroke-width="1.6"/><path d="M2 3l10 8 10-8" fill="none" stroke="#fff" stroke-width="1.6"/></svg>
      <p class="abs" style="left:57px;top:114px;width:190px;font-size:8.5px;line-height:12.5px">website: www.tessapinlowe.com<br><br>Linden Row House – A Boutique Art Hotel Address:<br>2817 Elm Ridge Ave, Riverton, MO 64199</p>
      <div class="f-rule abs" style="left:20px;top:195px;width:223px"></div>
      <p class="abs" style="left:27px;top:212px;font-size:13px">Follow us</p>
      <span class="abs" style="left:100px;top:213px;width:13px;height:13px;border-radius:50%;background:#fff"></span>
      <span class="abs" style="left:129px;top:213px;width:13px;height:13px;border-radius:50%;background:#fff"></span>
      <span class="abs" style="left:158px;top:213px;width:13px;height:13px;border-radius:50%;background:#fff"></span>
      <span class="abs" style="left:187px;top:213px;width:13px;height:13px;border-radius:50%;background:#fff"></span>
    </div>
  </footer>

</main>
</body>
</html>
```